Renewed electronic office supplies

I need a landing page design for a B2B business that will sell refurbished and renewed electronic devices such as smartphones, laptops, tablets and other gadgets. We want to become suppliers of these devices to companies that need computers and other devices for their employees. The point of our business is that they can get a great device that is in very good contrition instead of buying brand new. Companies will be able to save 50-60% on these renewed devices. Not only that we will also buy the companies old devices which they no longe needs and renew them and give them new life so we can resell it.

Our services will be:

- sale of renewed devices with lifetime warranty

- purchase of old devices

- swap solution: meaning client buy from us and sell at the same time so we deduct the amount sale of their old devices into their purchase.

Some useful information:

- company name and logo are still pending

- we aim to provide all business with top quality of renewed and environmentally friendly electronics, while maintaining a minimal impact on the natural environment.

I have attached a word document with some additional info that might be useful

Looking forward to seeing all your great designs!

P.s. Please feel free to make designs that are not based on my documents also, we need different layouts and designs. as for now I see many of the designs are more or less the same. we need more variation on design
Updates

Target Market(s)

Medium to large Businesses

Industry/Entity Type

Technology Equipment

Requirements
Must have
• we need more designs to be submitted , 50 designs minimum

```html
<!DOCTYPE html>
<html lang="en">
<head>
<meta charset="UTF-8">
<title>Renewtek Global – Reusable Electronic Office Supplies</title>
<link href="https://fonts.googleapis.com/css2?family=Jost:ital,wght@0,400;0,500;1,400&display=swap" rel="stylesheet">
<style>
:root{
  --violet:#7a0aa8;
  --indigo:#2a0fb0;
  --deep:#1e0d9e;
  --royal:#1d0fa8;
  --white:#ffffff;
  --ink:#222222;
  --body:#444444;
  --muted:#888888;
  --link:#1d18a0;
}
*{margin:0;padding:0;box-sizing:border-box}
html,body{width:1200px;height:2564px;overflow:hidden}
body{position:relative;background:var(--white);font-family:'Jost',sans-serif;color:var(--ink)}
.abs{position:absolute}

/* hero */
.hero-shape{position:absolute;left:0;top:0;width:1200px;height:680px}
.brand{left:111px;top:44px;font-size:31px;color:var(--white);font-weight:400}
.nav{top:58px;left:614px;display:flex;gap:43px;font-size:16px;color:var(--white)}
.hero-title{left:111px;top:200px;font-size:43px;line-height:56px;color:var(--white);font-weight:500;letter-spacing:.3px}
.hero-text{left:114px;top:324px;width:470px;font-size:18px;line-height:35.5px;color:var(--white)}
.shop-btn{left:117px;top:451px;width:162px;height:59px;border:2px solid var(--white);border-radius:30px;color:var(--white);font-size:18px;display:flex;align-items:center;justify-content:center;font-weight:500}
.hero-media{left:595px;top:210px;width:582px;height:330px;border-radius:14px 14px 4px 4px;background:linear-gradient(180deg,#d9d9d9 0%,#bdbdbd 100%);padding:26px 26px 38px}
.hero-media .screen{width:100%;height:100%;background:radial-gradient(circle at 45% 40%,#3a4e86 0%,#141a3c 55%,#070a1e 100%)}

/* categories */
.cat{top:805px;width:238px;height:241px;border-radius:6px;overflow:hidden;display:flex;align-items:flex-end;justify-content:center;padding-bottom:20px;color:var(--white);font-size:24px}
.cat-phone{left:112px;background:linear-gradient(160deg,#6f7a86 0%,#3b3f46 55%,#1c1d22 100%)}
.cat-laptop{left:360px;background:linear-gradient(170deg,#a97858 0%,#5b4638 45%,#1f1b19 100%)}
.cat-tablet{left:608px;background:linear-gradient(160deg,#5e7482 0%,#3b4b58 55%,#1d2329 100%)}
.cat-gadget{left:856px;background:linear-gradient(170deg,#8a7a68 0%,#54504a 50%,#242220 100%)}

/* about */
.about-kicker{left:112px;top:1137px;font-size:19px;font-style:italic;color:var(--muted)}
.about-title{left:112px;top:1162px;width:480px;font-size:30px;line-height:41px;color:var(--ink)}
.about-copy{left:112px;width:480px;font-size:15px;line-height:29.3px;color:var(--body);text-align:justify}
.about-sub{left:111px;font-size:20px;color:var(--link)}
.about-circle{left:651px;top:1225px;width:438px;height:438px;border-radius:50%;background:var(--royal)}
.about-media{left:760px;top:1185px;width:250px;height:515px;border-radius:34px;background:linear-gradient(170deg,#1e2d88 0%,#3b1a6e 35%,#c81e4a 75%,#e02a52 100%);transform:rotate(8deg);border:8px solid #141414}

/* services */
.services{left:0;top:1779px;width:1200px;height:514px;background:linear-gradient(120deg,#6a0ca6 0%,#3d0db0 45%,#2410a8 100%)}
.services-title{left:0;top:1812px;width:1200px;text-align:center;font-size:42px;color:var(--white);font-weight:500}
.services-rule{left:574px;top:1874px;width:58px;height:3px;background:var(--white)}
.svc{top:1930px;width:210px;text-align:center;color:var(--white)}
.svc .ring{width:136px;height:136px;border:2px solid var(--white);border-radius:50%;margin:0 auto;display:flex;align-items:center;justify-content:center}
.svc p{margin-top:20px;font-size:15px;line-height:29.3px}

/* footer */
.foot-brand{left:0;top:2345px;width:1200px;text-align:center;font-size:34px;color:var(--link)}
.foot-nav{left:0;top:2414px;width:1200px;display:flex;justify-content:center;gap:60px;font-size:16px;color:var(--ink)}
.social{left:504px;top:2464px;display:flex;gap:6px}
.social span{width:34px;height:34px;border:1.5px solid #333;border-radius:50%}
.copyright{left:0;top:2525px;width:1200px;text-align:center;font-size:15px;color:var(--ink)}
</style>
</head>
<body>

<svg class="hero-shape" viewBox="0 0 1200 680" aria-hidden="true">
  <defs>
    <linearGradient id="heroGrad" x1="0" y1="0" x2="1" y2="1">
      <stop offset="0" stop-color="#7a0aa8"/>
      <stop offset=".5" stop-color="#3f0cae"/>
      <stop offset="1" stop-color="#1e0d9e"/>
    </linearGradient>
  </defs>
  <path d="M0 0H1200V295C1120 380 950 450 720 540C560 610 450 672 340 672C150 672 60 540 0 400Z" fill="url(#heroGrad)"/>
</svg>

<div class="abs brand">Renewtek Global</div>
<nav class="abs nav"><span>Home</span><span>About Us</span><span>Services</span><span>News</span><span>Contact Us</span></nav>

<h1 class="abs hero-title">REUSABLE ELECTRONIC<br>OFFICE SUPPLIES</h1>
<p class="abs hero-text">We aim to provide all business with top quality of reused &amp; environmentally friendly electronics, while maintaining a minimal impact on the natural environment.</p>
<div class="abs shop-btn">SHOP</div>
<div class="abs hero-media" role="img" aria-label="Open laptop showing a starry virtual reality scene"><div class="screen"></div></div>

<div class="abs cat cat-phone" role="img" aria-label="Hands using a smartphone">Smartphones</div>
<div class="abs cat cat-laptop" role="img" aria-label="Laptop on a desk">Laptops</div>
<div class="abs cat cat-tablet" role="img" aria-label="Hands holding a tablet">Tablets</div>
<div class="abs cat cat-gadget" role="img" aria-label="Laptop and phone on a table">Gadgets</div>

<div class="abs about-kicker">We are</div>
<h2 class="abs about-title" style="font-weight:400">A smarter circular solution for electronic supplies</h2>
<p class="abs about-copy" style="top:1256px">Billions of electronics are being made, sold, and disposed of every year — a cycle that drives short-term profits for electronics manufacturers, but at too high a cost for the planet we all share. With our experience in the recycling market we can put an end to this cycle and offer a circular solution that is both affordable and environmentally friendly.</p>
<h3 class="abs about-sub" style="top:1420px;font-weight:400">Buy reusable IT</h3>
<p class="abs about-copy" style="top:1459px">We specialize in refurbished electronic devices with top quality affordable prices. All our products have undergone a detailed testing &amp; reconditioning program by expert technicians.</p>
<h3 class="abs about-sub" style="top:1567px;font-weight:400">Sell your IT Safely</h3>
<p class="abs about-copy" style="top:1609px;text-align:left">We can also buy your used electronics and make sure they get reused and give them a new life. By selling your used devices that you no longer have use for you can help us create carbon savings.</p>
<div class="abs about-circle"></div>
<div class="abs about-media" role="img" aria-label="Smartphone with a colourful lock screen"></div>

<section class="abs services"></section>
<h2 class="abs services-title">Our Services</h2>
<div class="abs services-rule"></div>

<div class="abs svc" style="left:129px">
  <div class="ring"><svg width="70" height="70" viewBox="0 0 70 70" fill="none" stroke="#fff" stroke-width="2.5"><circle cx="35" cy="35" r="28"/><circle cx="35" cy="35" r="18"/><path d="M27 35l6 6 11-12"/></svg></div>
  <p>Sale of renewed devices with lifetime warranty</p>
</div>
<div class="abs svc" style="left:378px">
  <div class="ring"><svg width="70" height="70" viewBox="0 0 70 70" fill="none" stroke="#fff" stroke-width="2.5"><rect x="14" y="20" width="42" height="28" rx="2"/><path d="M8 52h54"/><path d="M35 12v26M29 32l6 6 6-6"/></svg></div>
  <p>Purchase of old devices</p>
</div>
<div class="abs svc" style="left:626px">
  <div class="ring"><svg width="70" height="70" viewBox="0 0 70 70" fill="none" stroke="#fff" stroke-width="2.5"><path d="M14 26h38l-8-8M56 44H18l8 8"/></svg></div>
  <p>Swap solution: meaning clients buy from us and sell at the same time so we deduct the amount sale of their old devices into their purchase.</p>
</div>
<div class="abs svc" style="left:875px">
  <div class="ring"><svg width="70" height="70" viewBox="0 0 70 70" fill="none" stroke="#fff" stroke-width="2.5"><circle cx="35" cy="35" r="26"/><path d="M9 35h52M35 9c10 10 10 42 0 52M35 9c-10 10-10 42 0 52"/></svg></div>
  <p>We aim to provide all businesses with top quality of renewed and environmentally friendly electronics, while maintaining a minimal impact on the natural environment.</p>
</div>

<footer>
  <div class="abs foot-brand">Renewtek Global</div>
  <nav class="abs foot-nav"><span>Home</span><span>About Us</span><span>Services</span><span>News</span><span>Contact Us</span></nav>
  <div class="abs social" aria-label="Social links"><span></span><span></span><span></span><span></span><span></span></div>
  <div class="abs copyright">© Copyrights 2020-Renewtek Global.All Rights Reserved.</div>
</footer>

</body>
</html>
```